Candle company needs a label for candle

Looking for a designer to create my candle label. I am going to attach a few pictures of my vision for the label as well as my Company Logo and jar I have puchased. I'm going for the modern rustic feel but you are the designer and have full trust in your abilities. The label is going to be printed on Kraft paper (2x3) so looking for the font to be black. The candle label MUST include the following information:
Wick Harbor Co.
NO. 01: Eucalyptus + Spearmint
Handmade In NJ
Soy Wax
9oz

Industry/Entity Type

Candle Industry

Colors

Designer to choose colors to be used in the design.

Requirements
Should not have
• Any images

```html
<!DOCTYPE html>
<html lang="en">
<head>
<meta charset="utf-8">
<title>Wick Harbor Co. — Label Options</title>
<link href="https://fonts.googleapis.com/css2?family=Abril+Fatface&family=Montserrat:wght@400;500;700&display=swap" rel="stylesheet">
<style>
  :root {
    --board: #d4e6e6;
    --paper: #ffffff;
    --kraft: #cdb98f;
    --ink: #111111;
    --foliage: #3a3a3a;
  }
  * { margin: 0; padding: 0; box-sizing: border-box; }
  html, body { width: 1200px; height: 906px; overflow: hidden; }
  body {
    position: relative;
    background: var(--board);
    font-family: "Montserrat", Arial, sans-serif;
    color: var(--ink);
  }
  .option-title {
    position: absolute;
    font-size: 14px;
    font-weight: 700;
    letter-spacing: 4px;
  }
  .label {
    position: absolute;
    width: 241px;
    height: 360px;
    background: var(--paper);
  }
  .label > * { position: absolute; }

  .brand {
    display: flex;
    align-items: flex-start;
    gap: 6px;
    font-weight: 400;
    letter-spacing: 2.5px;
    line-height: 1.2;
    text-transform: uppercase;
  }
  .brand-mark {
    flex: none;
    width: 8px;
    height: 8px;
    background: var(--ink);
    margin-top: 4px;
  }
  .brand--md { font-size: 16px; }
  .brand--sm { font-size: 11px; }
  .brand--sm .brand-mark { width: 6px; height: 6px; margin-top: 3px; }

  .scent-no { font-size: 14px; font-weight: 700; }
  .scent-name { font-size: 21px; font-weight: 700; line-height: 28px; }
  .details { font-size: 13px; line-height: 16px; }

  /* Option 2 serif */
  .serif-title {
    font-family: "Abril Fatface", Georgia, serif;
    font-size: 33px;
    line-height: 40px;
  }
  .serif-title .plus { font-family: "Montserrat", Arial, sans-serif; font-weight: 400; font-size: 26px; }

  /* Ruled stack (options 3, 4 and kraft) */
  .ruled { display: flex; flex-direction: column; }
  .ruled .rule { height: 1px; background: var(--ink); }
  .ruled .row { font-size: 12.5px; line-height: 16px; padding: 8px 0; }
  .centered { text-align: center; align-items: center; }

  .foliage {
    left: 28px; top: 183px; width: 150px; height: 62px;
    background: linear-gradient(90deg, var(--foliage) 0%, #5a5a5a 60%, var(--foliage) 100%);
    border-radius: 30px;
    opacity: .85;
  }

  .kraft {
    position: absolute;
    left: 755px; top: 319px;
    width: 285px; height: 360px;
    background: var(--kraft);
  }
  .kraft > * { position: absolute; }

  .corner-brand {
    position: absolute;
    left: 1000px; top: 770px;
    font-size: 22px;
  }
  .corner-brand .brand-mark { width: 12px; height: 12px; margin-top: 6px; }
</style>
</head>
<body>

  <div class="option-title" style="left:79px; top:50px;">OPTION 1</div>
  <section class="label" style="left:79px; top:80px;">
    <div class="brand brand--md" style="left:20px; top:22px;"><span class="brand-mark"></span><span>Wick<br>Harbor Co.</span></div>
    <div class="scent-no" style="left:20px; top:145px;">NO. 01:</div>
    <div class="scent-name" style="left:20px; top:162px;">EUCALYPTUS +<br>SPEARMINT</div>
    <div class="details" style="left:20px; top:292px;">Handmade In NJ<br>Soy Wax<br>9oz</div>
  </section>

  <div class="option-title" style="left:360px; top:50px;">OPTION 2</div>
  <section class="label" style="left:360px; top:80px;">
    <div class="brand brand--md" style="left:20px; top:22px;"><span class="brand-mark"></span><span>Wick<br>Harbor Co.</span></div>
    <div class="serif-title" style="left:20px; top:118px;">NO. 01:<br>Eucalyptus <span class="plus">+</span><br>Spearmint</div>
    <div class="details" style="left:20px; top:292px;">Handmade In NJ<br>Soy Wax<br>9oz</div>
  </section>

  <div class="option-title" style="left:79px; top:463px;">OPTION 3</div>
  <section class="label" style="left:79px; top:492px;">
    <div class="brand brand--sm" style="left:26px; top:24px;"><span class="brand-mark"></span><span>Wick<br>Harbor Co.</span></div>
    <div class="scent-no" style="left:26px; top:84px;">NO. 01:</div>
    <div class="scent-name" style="left:26px; top:102px; font-size:23px; line-height:29px;">EUCALYPTUS<br>+ SPEARMINT</div>
    <div class="ruled" style="left:26px; top:165px; width:158px;"><div class="rule"></div></div>
    <div class="foliage" role="img" aria-label="Eucalyptus sprig and mint leaf illustration"></div>
    <div class="ruled" style="left:26px; top:263px; width:158px;">
      <div class="row" style="padding-top:0;">HANDMADE IN NJ</div>
      <div class="rule"></div>
      <div class="row">SOY WAX</div>
      <div class="rule"></div>
      <div class="row">9oz</div>
    </div>
  </section>

  <div class="option-title" style="left:356px; top:463px;">OPTION 4</div>
  <section class="label" style="left:359px; top:492px;">
    <div class="brand brand--md" style="left:62px; top:50px;"><span class="brand-mark"></span><span>Wick<br>Harbor Co.</span></div>
    <div class="ruled centered" style="left:36px; top:146px; width:159px;">
      <div class="scent-no" style="position:static; padding-bottom:8px;">NO. 01:</div>
      <div class="rule" style="width:100%;"></div>
      <div class="scent-name" style="position:static; padding:3px 0; font-size:22px; line-height:29px;">EUCALYPTUS<br>+ SPEARMINT</div>
      <div class="rule" style="width:100%;"></div>
      <div class="row">HANDMADE IN NJ</div>
      <div class="rule" style="width:100%;"></div>
      <div class="row">SOY WAX</div>
      <div class="rule" style="width:100%;"></div>
      <div class="row">9oz</div>
    </div>
  </section>

  <section class="kraft">
    <div class="brand brand--md" style="left:80px; top:60px;"><span class="brand-mark"></span><span>Wick<br>Harbor Co.</span></div>
    <div class="ruled centered" style="left:38px; top:150px; width:209px;">
      <div class="scent-no" style="position:static; padding-bottom:8px;">NO. 01:</div>
      <div class="rule" style="width:100%;"></div>
      <div class="scent-name" style="position:static; padding:4px 0; font-size:24px; line-height:30px;">EUCALYPTUS<br>+ SPEARMINT</div>
      <div class="rule" style="width:100%;"></div>
      <div class="row">HANDMADE IN NJ</div>
      <div class="rule" style="width:100%;"></div>
      <div class="row">SOY WAX</div>
      <div class="rule" style="width:100%;"></div>
      <div class="row">9oz</div>
    </div>
  </section>

  <div class="brand corner-brand"><span class="brand-mark"></span><span>Wick<br>Harbor Co.</span></div>

</body>
</html>
```